Business Cards for new orthopaedic surgery practice

My husband and I are starting our own orthopaedic surgery practice. We are looking for a business card that is uniform, but one will have my name/title and the other will have his. You can just create one design with my name on it for now. But when I choose your design as the winning design I will ask that you add another copy with his name/title.

We are looking for classy, simple, elite all in one. We like dark blues/a little gold/yellow. Something that goes with our logo. We want our logo incorporated. Here is all the info you need:
Business name: RV Spine & Vitality Center
Location: 38915 North Bramble Ave
Maple Hollow, FL 33990
Phone: 954-218-4630
Fax: 954-571-2846
Email: info@myrvspine.example

Names: Lucinda Ferrow, M.D.
Board Certified Wrist and Upper Limb Surgeon

Emeka Dlunga, M.D.
Board Certified Hip & Knee Replacement/General Orthopaedic Surgeon

Can decide what you want to put on the back. Maybe a slogan:
Rooted in Care. Focused on You

I am just going to upload our logo. The only thing is if we select you as the winning design, the location, and phone numbers may change. We will need your help to update that once fully solidified.

Industry/Entity Type

Medical

Contact Information for Business Card

Colors
0054AA
0677BA
7BADD7
CADEEF
E8F1F8
0094D4
00A9DD
6FCCEA
C7EBF8
E9F6FB

Requirements
Must have
• class, appeal,
Should not have
• We want to air on the side of masculine if we are looking at masculine vs. feminine feel. But we still want it classy, sophisticated, and something we will love

```html
<!DOCTYPE html>
<html lang="en">
<head>
<meta charset="utf-8">
<title>RV Spine &amp; Vitality Center – Business Card</title>
<link href="https://fonts.googleapis.com/css2?family=Lexend:wght@500;600&display=swap" rel="stylesheet">
<style>
  :root {
    --navy: #233d82;
    --cyan: #16b9e0;
    --paper-light: #e9ecfb;
    --paper-deep: #d4e2f9;
    --gap: #ffffff;
  }
  * { margin: 0; padding: 0; box-sizing: border-box; }
  html, body {
    width: 946px; height: 1200px; overflow: hidden;
    background: var(--gap);
    font-family: "Lexend", sans-serif;
  }
  .canvas { position: relative; width: 946px; height: 1200px; }
  .card {
    position: absolute; left: 0; width: 946px; height: 553px; overflow: hidden;
    background: linear-gradient(160deg, var(--paper-light) 0%, var(--paper-deep) 100%);
  }
  .card--front { top: 0; }
  .card--back { top: 647px; }
  .card-waves { position: absolute; inset: 0; width: 100%; height: 100%; }

  .brand {
    position: absolute; left: 0; right: 0; top: 150px;
    display: flex; flex-direction: column; align-items: center;
    color: var(--navy);
  }
  .brand-dot {
    width: 96px; height: 96px; border-radius: 50%;
    background: var(--navy); margin-bottom: 26px;
  }
  .brand-name {
    font-weight: 600; font-size: 40px; letter-spacing: 1px;
    text-transform: uppercase; text-align: center; line-height: 1.2;
  }

  .person { position: absolute; right: 74px; top: 90px; text-align: right; }
  .person-name {
    font-weight: 600; font-size: 39px; letter-spacing: 1.5px;
    color: var(--navy); line-height: 1;
  }
  .person-title {
    margin-top: 12px; font-weight: 500; font-size: 10.5px;
    letter-spacing: 1px; color: var(--cyan);
  }

  .contact { position: absolute; right: 72px; top: 240px; list-style: none; }
  .contact-item {
    display: flex; align-items: center; justify-content: flex-end;
    gap: 20px; margin-bottom: 22px;
    font-weight: 600; font-size: 26px; letter-spacing: 1.6px;
    color: var(--navy); text-align: right; line-height: 1.4;
  }
  .contact-item:nth-child(3) { margin-bottom: 12px; }
  .contact-icon { width: 36px; height: 36px; flex: none; }
</style>
</head>
<body>
<div class="canvas">

  <section class="card card--front">
    <svg class="card-waves" viewBox="0 0 987 576" preserveAspectRatio="none" aria-hidden="true">
      <path fill="var(--navy)" d="M0,0 H305 C285,70 230,92 150,122 C80,150 35,210 0,320 Z"/>
      <path fill="var(--cyan)" d="M0,0 H305 C292,50 255,80 200,96 C120,122 55,160 0,232 Z"/>
      <path fill="var(--navy)" d="M987,310 C930,345 870,360 830,398 C795,435 788,490 785,576 H987 Z"/>
      <path fill="var(--cyan)" d="M987,362 C922,385 862,400 832,432 C802,462 792,512 788,576 H987 Z"/>
    </svg>
    <div class="brand">
      <div class="brand-dot"></div>
      <p class="brand-name">RV Spine &amp; Vitality<br>Center</p>
    </div>
  </section>

  <section class="card card--back">
    <svg class="card-waves" viewBox="0 0 987 577" preserveAspectRatio="none" aria-hidden="true">
      <path fill="var(--navy)" d="M0,0 H365 C372,90 335,195 262,285 C180,385 92,445 84,577 H0 Z"/>
      <path fill="var(--cyan)" d="M0,0 H300 C306,95 272,195 212,275 C142,365 82,445 90,577 H0 Z"/>
    </svg>

    <div class="person">
      <h1 class="person-name">Lucinda Ferrow, M.D.</h1>
      <p class="person-title">Board Certified Wrist and Upper Limb Surgeon</p>
    </div>

    <ul class="contact">
      <li class="contact-item">
        <span>954-218-4630</span>
        <svg class="contact-icon" viewBox="0 0 36 36" aria-label="Phone">
          <circle cx="18" cy="18" r="18" fill="var(--navy)"/>
          <path fill="#fff" d="M12.5 9.5c.6-.4 1.4-.3 1.8.3l2 3c.4.6.3 1.3-.2 1.8l-1.2 1.1c.9 2 2.4 3.5 4.4 4.4l1.1-1.2c.5-.5 1.2-.6 1.8-.2l3 2c.6.4.7 1.2.3 1.8l-1.2 1.7c-.6.8-1.6 1.1-2.5.8-5-1.6-8.9-5.5-10.5-10.5-.3-.9 0-1.9.8-2.5z"/>
        </svg>
      </li>
      <li class="contact-item">
        <span>954-571-2846</span>
        <svg class="contact-icon" viewBox="0 0 36 36" aria-label="Fax">
          <circle cx="18" cy="18" r="18" fill="var(--navy)"/>
          <rect x="12.5" y="9" width="11" height="5" fill="#fff"/>
          <rect x="9" y="15" width="18" height="9" rx="2" fill="#fff"/>
          <rect x="12.5" y="20" width="11" height="7" fill="#fff" stroke="var(--navy)" stroke-width="1.5"/>
        </svg>
      </li>
      <li class="contact-item">
        <span>info@myrvspine.example</span>
        <svg class="contact-icon" viewBox="0 0 36 36" aria-label="Email">
          <circle cx="18" cy="18" r="18" fill="var(--navy)"/>
          <rect x="9" y="11.5" width="18" height="13" rx="1.5" fill="#fff"/>
          <path d="M9.5 12.5 L18 19 L26.5 12.5 M9.5 23.5 L15.5 17.5 M26.5 23.5 L20.5 17.5" fill="none" stroke="var(--navy)" stroke-width="1.5"/>
        </svg>
      </li>
      <li class="contact-item">
        <span>38915 North Bramble Ave<br>Maple Hollow, FL 33990</span>
        <svg class="contact-icon" viewBox="0 0 36 36" aria-label="Address">
          <circle cx="18" cy="18" r="18" fill="var(--navy)"/>
          <path fill="#fff" d="M18 8c-4 0-7 3-7 7 0 5 7 13 7 13s7-8 7-13c0-4-3-7-7-7zm0 9.6a2.6 2.6 0 1 1 0-5.2 2.6 2.6 0 0 1 0 5.2z"/>
        </svg>
      </li>
    </ul>
  </section>

</div>
</body>
</html>
```